Brightmoor Notes To Do List

I am looking to design a new "Study To Do List" for High School students (Ages 15 - 18) . This will be printed as an A4 notepad and so should only be a single A4 page.

The Design will need to be professional and look semi-serious but also be appealing to High school students (Ages 15 - 18) and should NOT be gender specific.

I have attached a word document outlining the structure of the page. The space provided should be large enough that people can write in it comfortably.

The notepad will most likely be printed in black and white but I'm also looking at coloured options - colours should be kept to a minimum.

This will be printed professionally and should also include a 3mm bleed.

The design should also include the business logo (included in the word document)

Target Market(s)

High School students (Ages 15 - 18). Both genders

Industry/Entity Type

Education

Font styles to use
Serif
Sans Serif

Requirements
Must have
• Please see the word document attached.
Should not have
• Too much colour

```html
<!DOCTYPE html>
<html lang="en">
<head>
<meta charset="utf-8">
<title>Brightmoor Notes – To Do List</title>
<link rel="stylesheet" href="https://fonts.googleapis.com/css2?family=Chewy&family=Montserrat:wght@700;800&display=swap">
<style>
  :root {
    --backdrop: #d9c0a4;
    --paper: #f7f7f6;
    --ink: #1d1d1d;
    --accent: #f0722c;
    --rule: #2a2a2a;
    --dash: #8a8a8a;
  }
  * { box-sizing: border-box; margin: 0; padding: 0; }
  html, body { width: 1200px; height: 900px; overflow: hidden; }
  body { background: var(--backdrop); position: relative; font-family: "Montserrat", sans-serif; color: var(--ink); }

  .sheet {
    position: absolute; left: 296px; top: 20px; width: 608px; height: 860px;
    background: var(--paper); padding: 22px 34px 26px;
    box-shadow: 0 6px 18px rgba(80, 50, 20, .18);
    display: flex; flex-direction: column;
  }

  .sheet-header { display: flex; align-items: center; justify-content: space-between; height: 44px; }
  .brand { display: flex; align-items: center; gap: 6px; font-size: 10px; font-weight: 800; }
  .brand-dot { width: 16px; height: 16px; border-radius: 50%; background: var(--accent); }
  .sheet-title { font-family: "Chewy", cursive; font-size: 28px; letter-spacing: 1px; }
  .date-field { font-family: "Chewy", cursive; font-size: 22px; display: flex; align-items: flex-end; gap: 4px; }
  .date-line { width: 90px; border-bottom: 2px solid var(--ink); height: 18px; }

  .section-heading {
    font-family: "Chewy", cursive; font-size: 22px; color: var(--accent);
    -webkit-text-stroke: .6px var(--ink); letter-spacing: .5px; line-height: 1; margin: 8px 0 4px;
  }

  .label { font-size: 7px; font-weight: 800; text-transform: uppercase; letter-spacing: .3px; }

  /* Revision */
  .revision-box { display: grid; grid-template-columns: 1fr 1fr; gap: 0 14px; border: 1px dashed var(--dash); padding: 4px 8px; }
  .revision-line { height: 24px; border-bottom: 1px dashed var(--dash); display: flex; align-items: flex-end; padding-bottom: 3px; }

  /* Homework */
  .homework-table, .assessment-table { border: 1px solid var(--rule); }
  .homework-row { display: grid; grid-template-columns: 1fr 1fr; height: 30px; border-bottom: 1px solid var(--rule); }
  .homework-row:last-child { border-bottom: none; }
  .homework-cell { padding: 4px 6px; }
  .homework-cell + .homework-cell { border-left: 1px solid var(--rule); }

  /* Assessments */
  .assessment-group { display: grid; grid-template-columns: 1fr 84px; border-bottom: 1.5px solid var(--rule); }
  .assessment-group:last-child { border-bottom: none; }
  .assessment-line { height: 21px; padding: 3px 6px; border-bottom: 1px solid var(--rule); grid-column: 1 / 3; }
  .element-line { height: 21px; padding: 3px 6px; }
  .due-cell { height: 21px; padding: 3px 6px; border-left: 1px solid var(--rule); }

  /* Notes & practice */
  .closing-row { display: grid; grid-template-columns: 1fr 1fr; gap: 0 16px; flex: 1; }
  .notes-grid { display: grid; grid-template-columns: 1fr 1fr; gap: 0 12px; }
  .notes-line { height: 27px; border-bottom: 1px dashed var(--dash); display: flex; align-items: flex-end; padding-bottom: 3px; }
  .practice-box { border: 1px solid var(--rule); height: 110px; display: flex; flex-direction: column; }
  .practice-line { flex: 1; border-bottom: 1px solid var(--rule); }
  .practice-line:last-child { border-bottom: none; }
</style>
</head>
<body>
<main class="sheet">
  <header class="sheet-header">
    <div class="brand"><span class="brand-dot"></span>Brightmoor Notes</div>
    <h1 class="sheet-title">to do list</h1>
    <div class="date-field">Date:<span class="date-line"></span></div>
  </header>

  <section class="revision">
    <h2 class="section-heading">revision</h2>
    <div class="revision-box">
      <div>
        <div class="revision-line label">1.</div>
        <div class="revision-line label">2.</div>
        <div class="revision-line label">3.</div>
        <div class="revision-line label">4.</div>
      </div>
      <div>
        <div class="revision-line label">5.</div>
        <div class="revision-line label">6.</div>
        <div class="revision-line label">7.</div>
        <div class="revision-line label">8.</div>
      </div>
    </div>
  </section>

  <section class="homework">
    <h2 class="section-heading">Homework</h2>
    <div class="homework-table">
      <div class="homework-row"><div class="homework-cell label">Subject:</div><div class="homework-cell label">Task:</div></div>
      <div class="homework-row"><div class="homework-cell label">Subject:</div><div class="homework-cell label">Task:</div></div>
      <div class="homework-row"><div class="homework-cell label">Subject:</div><div class="homework-cell label">Task:</div></div>
      <div class="homework-row"><div class="homework-cell label">Subject:</div><div class="homework-cell label">Task:</div></div>
      <div class="homework-row"><div class="homework-cell label">Subject:</div><div class="homework-cell label">Task:</div></div>
      <div class="homework-row"><div class="homework-cell label">Subject:</div><div class="homework-cell label">Task:</div></div>
    </div>
  </section>

  <section class="assessments">
    <h2 class="section-heading">assessments</h2>
    <div class="assessment-table">
      <div class="assessment-group"><div class="assessment-line label">Assessment:</div><div class="element-line label">Element:</div><div class="due-cell label">Due:</div></div>
      <div class="assessment-group"><div class="assessment-line label">Assessment:</div><div class="element-line label">Element:</div><div class="due-cell label">Due:</div></div>
      <div class="assessment-group"><div class="assessment-line label">Assessment:</div><div class="element-line label">Element:</div><div class="due-cell label">Due:</div></div>
      <div class="assessment-group"><div class="assessment-line label">Assessment:</div><div class="element-line label">Element:</div><div class="due-cell label">Due:</div></div>
    </div>
  </section>

  <div class="closing-row">
    <section class="notes">
      <h2 class="section-heading">notes</h2>
      <div class="notes-grid">
        <div>
          <div class="notes-line label">1.</div>
          <div class="notes-line label">2.</div>
          <div class="notes-line label">3.</div>
          <div class="notes-line label">4.</div>
        </div>
        <div>
          <div class="notes-line label">5.</div>
          <div class="notes-line label">6.</div>
          <div class="notes-line label">7.</div>
          <div class="notes-line label">8.</div>
        </div>
      </div>
    </section>
    <section class="practice">
      <h2 class="section-heading">Practice!</h2>
      <div class="practice-box">
        <div class="practice-line"></div>
        <div class="practice-line"></div>
        <div class="practice-line"></div>
        <div class="practice-line"></div>
      </div>
    </section>
  </div>
</main>
</body>
</html>
```